Verdant Pathworks Business Card

want the back of card to be blue- with the logo in the center
front of card- info plus logo (info being mailing address, email address, and website address )
4 different names with titles to have on cards
1) Dominic Ashvale - Owner
2) Bethany Korvuth- Customer Relationship Specialist
3) Luca Brennwick- Vice President of Sales
4) Neil Umbright- Chief Technology Officer

Target Market(s)

tech company in the government/probation office industry

Industry/Entity Type

Government Office

Contact Information for Business Card

1) Dominic Ashvale - Owner

Colors
0355a3
ffffff

Requirements
Must have
• back side should be blue, with the logo placed in the center
• front side needs to include both the logo, as well as company info (info should include website address, email address, and mailing address)

```html
<!DOCTYPE html>
<html lang="en">
<head>
<meta charset="UTF-8">
<title>Verdant Pathworks Business Card</title>
<link href="https://fonts.googleapis.com/css2?family=Open+Sans:wght@400;600&display=swap" rel="stylesheet">
<style>
  :root {
    --brand-blue: #0355a3;
    --blue-light: #0a7cc4;
    --blue-deep: #033f86;
    --navy-mark: #1d3a6e;
    --white: #ffffff;
    --ink: #3a3a3a;
    --ink-soft: #6b6b6b;
    --stage: #e9ebee;
  }
  * { margin: 0; padding: 0; box-sizing: border-box; }
  html, body {
    width: 1200px;
    height: 900px;
    overflow: hidden;
    background: var(--stage);
    font-family: "Open Sans", Arial, sans-serif;
  }
  .canvas {
    position: relative;
    width: 1200px;
    height: 900px;
  }
  .card {
    position: absolute;
    left: 250px;
    width: 700px;
    height: 400px;
    overflow: hidden;
    box-shadow: 0 8px 24px rgba(0, 0, 0, 0.18);
  }
  .card--front { top: 30px; background: var(--white); }
  .card--back {
    top: 470px;
    background: radial-gradient(ellipse at 55% 30%, var(--blue-light) 0%, var(--brand-blue) 55%, var(--blue-deep) 100%);
    display: flex;
    align-items: center;
    justify-content: center;
  }

  /* Front */
  .front-panel {
    position: absolute;
    left: 0; top: 0;
    width: 265px;
    height: 100%;
    background: linear-gradient(180deg, var(--brand-blue) 0%, var(--blue-light) 100%);
    display: flex;
    align-items: center;
    justify-content: center;
  }
  .front-edge {
    position: absolute;
    right: 0; top: 0;
    width: 14px;
    height: 100%;
    background: var(--brand-blue);
  }
  .brand-name {
    font-family: "Open Sans", Arial, sans-serif;
    font-weight: 600;
    color: var(--navy-mark);
    text-align: center;
    letter-spacing: 1px;
    line-height: 1.15;
  }
  .front-panel .brand-name { font-size: 24px; }
  .card--back .brand-name { font-size: 44px; }

  .details {
    position: absolute;
    left: 318px;
    top: 46px;
    width: 340px;
  }
  .person-name {
    font-size: 34px;
    font-weight: 400;
    color: var(--ink);
    text-transform: uppercase;
    letter-spacing: 0.5px;
    padding-bottom: 4px;
    border-bottom: 3px solid var(--ink);
    white-space: nowrap;
  }
  .person-title {
    margin-top: 6px;
    font-size: 14px;
    color: var(--ink-soft);
    text-transform: uppercase;
    letter-spacing: 0.5px;
  }
  .address {
    margin-top: 20px;
    margin-left: 30px;
    font-size: 15px;
    line-height: 1.35;
    color: var(--ink-soft);
    font-style: normal;
  }
  .contact-list {
    list-style: none;
    margin-top: 34px;
    margin-left: 40px;
  }
  .contact-item {
    display: flex;
    align-items: center;
    gap: 14px;
    font-size: 15px;
    color: var(--ink);
    margin-bottom: 16px;
  }
  .contact-icon { width: 26px; height: 26px; flex: none; }
</style>
</head>
<body>
<main class="canvas">
  <section class="card card--front" aria-label="Card front">
    <div class="front-panel">
      <p class="brand-name">Verdant<br>Pathworks</p>
    </div>
    <div class="details">
      <h1 class="person-name">Dominic Ashvale</h1>
      <p class="person-title">Owner</p>
      <address class="address">
        1234,Address line 1,<br>
        Address line 2,<br>
        Address line 3
      </address>
      <ul class="contact-list">
        <li class="contact-item">
          <svg class="contact-icon" viewBox="0 0 26 26" aria-hidden="true">
            <circle cx="13" cy="13" r="11" fill="none" stroke="#222" stroke-width="2.2"/>
            <ellipse cx="13" cy="13" rx="5" ry="11" fill="none" stroke="#222" stroke-width="2"/>
            <line x1="2" y1="13" x2="24" y2="13" stroke="#222" stroke-width="2"/>
            <line x1="4" y1="8" x2="22" y2="8" stroke="#222" stroke-width="1.6"/>
            <line x1="4" y1="18" x2="22" y2="18" stroke="#222" stroke-width="1.6"/>
          </svg>
          <span>www.verdantpathworks.com</span>
        </li>
        <li class="contact-item">
          <svg class="contact-icon" viewBox="0 0 26 26" aria-hidden="true">
            <rect x="2" y="5" width="22" height="16" rx="2" fill="none" stroke="#222" stroke-width="2.2"/>
            <polyline points="3,7 13,15 23,7" fill="none" stroke="#222" stroke-width="2.2"/>
          </svg>
          <span>hello@verdantpathworks.com</span>
        </li>
      </ul>
    </div>
    <div class="front-edge"></div>
  </section>

  <section class="card card--back" aria-label="Card back">
    <p class="brand-name">Verdant Pathworks</p>
  </section>
</main>
</body>
</html>
```